Real Estate agent needs flyer/folder to contain bio and overview of services

I'm including files of the layout of the small folder. The folder is 6 1/2 across and 9 1/2 inches long. It will have a front & back cover and then writing on the 2 inside pages.

I am sending a few files to incorporate into the flyer, 1 new logo to use and 2 files which are coloring ideas.

```html
<!DOCTYPE html>
<html lang="en">
<head>
<meta charset="utf-8">
<title>Nora Castellane Realtor – Presentation Folder</title>
<link rel="stylesheet" href="https://fonts.googleapis.com/css2?family=Montserrat:ital,wght@0,400;0,500;0,600;1,400&display=swap">
<style>
  :root{
    --canvas:#e3e3e3;
    --canvas-alt:#dedede;
    --blue-deep:#0c2a8c;
    --blue:#1d4cc4;
    --blue-bright:#4b7fe6;
    --band:#1f4292;
    --heading:#2a55b8;
    --ink:#5a5f6a;
    --paper:#ffffff;
    --rule:#d3d8e2;
  }
  *{box-sizing:border-box;margin:0;padding:0}
  html,body{width:1200px;height:3600px;overflow:hidden;background:var(--canvas)}
  body{font-family:"Montserrat",Arial,sans-serif;color:var(--ink);position:relative}

  .stage{position:absolute;left:0;width:1200px;height:1200px;display:flex;align-items:center;justify-content:center}
  .stage--front{top:0}
  .stage--outside{top:1200px;background:var(--canvas-alt)}
  .stage--inside{top:2400px}

  .spread{display:flex;width:1080px;height:789px;box-shadow:0 30px 50px rgba(0,0,0,.18)}
  .panel{position:relative;width:540px;height:789px;overflow:hidden}

  /* Covers */
  .cover-bg{
    background:
      radial-gradient(ellipse 70% 40% at 30% 25%,rgba(120,160,255,.35),transparent 70%),
      radial-gradient(ellipse 60% 50% at 80% 75%,rgba(90,130,240,.30),transparent 70%),
      linear-gradient(160deg,var(--blue) 0%,var(--blue-deep) 55%,var(--blue) 100%);
    color:#fff;
  }
  .cover--front{border-radius:0 170px 170px 0}
  .front-solo{transform:scale(1.12);box-shadow:0 30px 50px rgba(0,0,0,.18)}

  .badge{position:absolute;left:50%;top:120px;width:290px;height:290px;margin-left:-145px}
  .badge__name{position:absolute;inset:0;display:flex;align-items:center;justify-content:center;text-align:center;
    font-weight:500;font-size:22px;letter-spacing:3px;line-height:1.35;color:var(--blue)}

  .tagline{position:absolute;left:0;right:0;top:470px;text-align:center;font-size:23px;font-weight:400;
    letter-spacing:1.5px;line-height:1.25;text-transform:uppercase}
  .cover-web{position:absolute;left:0;right:0;top:590px;text-align:center;font-size:14px;letter-spacing:4px}
  .cover-web::after{content:"";display:block;width:230px;height:2px;margin:14px auto 0;background:rgba(8,24,90,.55)}

  /* Back cover */
  .back-note{position:absolute;left:60px;right:50px;top:520px;font-size:13px;font-style:italic;line-height:1.5;text-align:justify}
  .back-footer{position:absolute;left:60px;top:620px;display:flex;align-items:center;gap:18px}
  .back-logo{width:120px;height:82px;background:var(--paper);display:flex;align-items:center;justify-content:center;
    text-align:center;font-size:11px;font-weight:500;letter-spacing:1px;color:var(--blue);line-height:1.3}
  .broker{display:flex;align-items:center;gap:6px;font-size:11px;font-weight:500;color:#fff;width:100px}
  .broker__dot{width:16px;height:16px;border-radius:50%;background:#fff;flex:none}
  .back-divider{width:1px;height:90px;background:rgba(255,255,255,.7)}
  .back-contact{font-size:14px;letter-spacing:2px;line-height:1.9}

  /* Inside */
  .inside-left{background:var(--paper);border-radius:170px 0 0 170px}
  .photo{position:absolute}
  .photo--porch{left:0;top:0;width:195px;height:789px;
    background:linear-gradient(180deg,#3a4150 0%,#2b3038 40%,#5a4a3a 65%,#3f5a34 100%)}
  .photo--agent{left:250px;top:610px;width:170px;height:179px;
    background:linear-gradient(180deg,#e8ecf2 0%,#d9c39a 45%,#2a2a30 100%)}
  .photo--lawn{left:330px;top:0;width:210px;height:620px;
    background:linear-gradient(180deg,#5aa0e0 0%,#9dc4ea 25%,#b9a98f 45%,#7d6a55 60%,#6ea040 80%,#4f8a2c 100%)}

  .column{position:absolute;top:52px}
  .column--left{left:225px;width:290px}
  .column--right{left:36px;width:272px}
  .section-title{font-size:12px;font-weight:600;letter-spacing:1px;color:var(--heading);text-transform:uppercase;margin:0 0 6px}
  .body-copy{font-size:9.5px;line-height:1.55;margin-bottom:16px}

  .quote{position:relative;border:1px solid var(--rule);padding:10px 10px 8px 28px;margin-bottom:12px;font-size:9.5px;font-style:italic;line-height:1.5}
  .quote::before{content:"\201C";position:absolute;left:8px;top:2px;font-size:26px;font-style:normal;color:var(--heading);font-weight:600}
  .quote__by{display:block;text-align:right;font-style:normal;font-weight:600;font-size:9px;margin-top:4px;color:#333}

  .agent-name{position:absolute;left:430px;top:650px;width:100px;font-size:12px;font-weight:500;letter-spacing:1px;line-height:1.35;color:var(--blue)}
  .broker-inside{position:absolute;left:95px;top:610px;display:flex;align-items:center;gap:8px;font-size:12px;font-weight:500;color:var(--blue)}
  .broker-inside .broker__dot{background:var(--blue)}

  .band{position:absolute;left:0;top:0;width:540px;height:789px}
  .inside-contact{position:absolute;right:34px;bottom:38px;text-align:right;color:#fff;font-size:14px;line-height:1.45;letter-spacing:.5px}
</style>
</head>
<body>

<!-- Front cover -->
<section class="stage stage--front">
  <div class="panel cover-bg cover--front front-solo">
    <div class="badge">
      <svg width="290" height="290" viewBox="0 0 290 290" aria-hidden="true">
        <polygon points="85,0 205,0 290,85 290,205 205,290 85,290 0,205 0,85" fill="rgba(20,50,150,.55)"/>
        <polygon points="93,20 197,20 270,93 270,197 197,270 93,270 20,197 20,93" fill="#fff"/>
      </svg>
      <div class="badge__name">NORA<br>CASTELLANE</div>
    </div>
    <p class="tagline">Let your search for<br>a real estate professional<br>end here</p>
    <p class="cover-web">www.norachomes.com</p>
  </div>
</section>

<!-- Outside spread -->
<section class="stage stage--outside">
  <div class="spread">
    <div class="panel cover-bg cover--back">
      <p class="back-note">Along with being your Realtor, I'm a lifelong resource for all things home-related &amp; beyond...if you need a great referral for anything at all, call me! I can't wait to work with you!</p>
      <div class="back-footer">
        <div class="back-logo">NORA<br>CASTELLANE</div>
        <div class="broker"><span class="broker__dot"></span>Summit Realty</div>
        <div class="back-divider"></div>
        <div class="back-contact">555-014-2237<br>nora@norachomes.com<br>www.norachomes.com</div>
      </div>
    </div>
    <div class="panel cover-bg cover--front">
      <div class="badge">
        <svg width="290" height="290" viewBox="0 0 290 290" aria-hidden="true">
          <polygon points="85,0 205,0 290,85 290,205 205,290 85,290 0,205 0,85" fill="rgba(20,50,150,.55)"/>
          <polygon points="93,20 197,20 270,93 270,197 197,270 93,270 20,197 20,93" fill="#fff"/>
        </svg>
        <div class="badge__name">NORA<br>CASTELLANE</div>
      </div>
      <p class="tagline">Let your search for<br>a real estate professional<br>end here</p>
      <p class="cover-web">www.norachomes.com</p>
    </div>
  </div>
</section>

<!-- Inside spread -->
<section class="stage stage--inside">
  <div class="spread">
    <div class="panel inside-left">
      <div class="photo photo--porch" role="img" aria-label="Photo of a house front porch at dusk with a stone walkway"></div>
      <div class="column column--left">
        <h2 class="section-title">Let me introduce myself</h2>
        <p class="body-copy">I have helped families across the county buy and sell homes for over fifteen years. I listen first, plan carefully and keep you informed at every step so each move feels calm and clear.</p>
        <h2 class="section-title">My core tenet</h2>
        <p class="body-copy">Your goals lead the way. I treat every client with honesty, patience and respect, whether it is a first condo or a forever home.</p>
        <h2 class="section-title">Real estate services &amp; beyond...</h2>
        <p class="body-copy">From pricing and staging to inspections, movers and trusted local trades, I connect you with the right people long after closing day.</p>
        <h2 class="section-title">Selling your home</h2>
        <p class="body-copy">A strong sale starts with a clear price and a great first look. I prepare your home, market it widely and negotiate firmly for the best result.</p>
      </div>
      <svg class="band" viewBox="0 0 540 789" aria-hidden="true">
        <polygon points="195,690 290,789 195,789" fill="var(--blue)"/>
      </svg>
      <div class="photo photo--agent" role="img" aria-label="Portrait photo of the realtor"></div>
      <div class="agent-name">NORA<br>CASTELLANE</div>
    </div>

    <div class="panel" style="background:var(--paper)">
      <div class="photo photo--lawn" role="img" aria-label="Photo of a single-storey home with a green lawn under blue sky"></div>
      <div class="column column--right">
        <h2 class="section-title">Buying a home</h2>
        <p class="body-copy">Finding the right home takes more than browsing listings. I help you set a budget, tour the best fits and write offers that stand out in a busy market. We will review every detail together so you can sign with confidence.</p>
        <h2 class="section-title">Testimonials:</h2>
        <p class="quote">She found us the perfect home in just three weeks and made the whole process easy and stress free.<span class="quote__by">Dana &amp; Joel Parker</span></p>
        <p class="quote">Nora sold our house above asking price. Her advice on staging and timing made all the difference.<span class="quote__by">Marcus &amp; Ellen Hale</span></p>
        <p class="quote">Knowledgeable, patient and always available. We would not trust anyone else with our next move.<span class="quote__by">Priya Sandoval</span></p>
      </div>
      <div class="broker-inside"><span class="broker__dot"></span>Summit Realty</div>
      <svg class="band" viewBox="0 0 540 789" aria-hidden="true">
        <polygon points="0,745 540,565 540,789 0,789" fill="var(--band)"/>
      </svg>
      <div class="inside-contact">555 014 2237<br>nora@norachomes.com<br>www.norachomes.com</div>
    </div>
  </div>
</section>

</body>
</html>
```